Crib Caller

This is a single-page full-screen tablet app that generates baby names based on a few user-selected options. The code is already written; I just need the visual design.
UI elements are:
1) Options, containing:
i) Gender selector
ii) Multi-select
inspiration sources (names based on country of origin)
iii) Scroll speed selector
2) Favourites panel containing list of current favourites (with UI to delete items)
3) Output panel; a live scrolling list of generated names - click to add as a favourite.
The app is a Windows 8 Metro application, written in XAML. It should stick to the Metro conventions/spirit. Here are some docs/samples:
http://docs.quellarion.com/library/tiles/apps/kq552918/
http://en.plexoverum.org/wiki/Lattice_(design_language)
Ideally, design will be presented in XAML format.
The attached design is the crap I've got meanwhile - it shows the basic elements. The list of generated names appears in the white-space on the right. The bar on the bottom is an advertisement.
More on the Metro design principles that should be adhered to:
http://www.quellarion.com/design/toolbox/tutorials/tiles-handset-4/lattice/
Ideal submission would be in XAML format. However, Adobe Illustrator files are decent as well; vector format is important.
Pixel-based images aren't ideal in this case, because Metro applications need to be scalable to any resolution.
Target Market(s)
People expecting a baby; mostly women.
Industry/Entity Type
Baby
Look and feel
Each slider illustrates characteristics of the customer's brand and the style your logo design should communicate.

```html
<!DOCTYPE html>
<html lang="en">
<head>
<meta charset="utf-8">
<title>Crib Caller</title>
<link rel="stylesheet" href="https://fonts.googleapis.com/css2?family=Pathway+Gothic+One&family=Lato:wght@400&display=swap">
<style>
  :root {
    --sky-top: #f7c4dd;
    --sky-mid: #c8b2e0;
    --sky-bottom: #76b6ef;
    --panel: #aaa9e3;
    --panel-deep: #9f9fdc;
    --tray: #b7b5ea;
    --label: #ffffff;
    --boy: #2f74c6;
    --girl: #ee6aa6;
    --output-top: #f3e2ee;
    --output-bottom: #cddff2;
    --ink-soft: #8a8a8c;
    --ink: #1c1c24;
    --rule: rgba(255,255,255,0.75);
    --index: #7d7d9a;
  }
  * { box-sizing: border-box; margin: 0; padding: 0; }
  html, body { width: 1200px; height: 585px; overflow: hidden; }
  body {
    position: relative;
    background: linear-gradient(180deg, var(--sky-top) 0%, var(--sky-mid) 50%, var(--sky-bottom) 100%);
    font-family: "Pathway Gothic One", "Arial Narrow", sans-serif;
    color: var(--label);
  }
  .backdrop { position: absolute; inset: 0; }
  .panel {
    position: absolute;
    background: var(--panel);
    box-shadow: 0 2px 6px rgba(60,60,120,0.25);
  }
  .panel-title {
    position: absolute; left: 15px; top: 12px;
    font-size: 22px; letter-spacing: 0.5px; text-transform: uppercase;
  }
  .gender { left: 47px; top: 93px; width: 168px; height: 146px; }
  .gender-button {
    position: absolute; top: 58px; width: 42px; height: 42px; border-radius: 50%;
    border: 1px solid rgba(255,255,255,0.7);
    box-shadow: 0 2px 3px rgba(60,60,120,0.3);
  }
  .gender-button.boy { left: 14px; background: radial-gradient(circle at 45% 35%, #d7f0ff, #7cc8f2 60%, #4fa8e0); }
  .gender-button.girl { left: 86px; background: radial-gradient(circle at 45% 35%, #ffd9ea, #f39ac3 60%, #e46ea6); }
  .gender-label { position: absolute; top: 111px; font-size: 15px; width: 60px; text-align: center; }
  .gender-label.boy { left: 5px; color: var(--boy); }
  .gender-label.girl { left: 77px; color: var(--girl); }

  .speed { left: 236px; top: 93px; width: 191px; height: 146px; }
  .speed-label { position: absolute; font-size: 15px; }
  .speed-label.slower { left: 10px; top: 32px; }
  .speed-label.faster { right: 8px; top: 89px; }
  .speed-track {
    position: absolute; left: 24px; top: 66px; width: 145px; height: 10px; border-radius: 5px;
    background: linear-gradient(90deg, #4f8fe0 0 48%, #f4f4f6 48%);
    border: 1px solid #8ba6d6;
  }
  .speed-knob {
    position: absolute; left: 83px; top: 57px; width: 28px; height: 28px; border-radius: 50%;
    background: radial-gradient(circle at 45% 35%, #ffffff, #dcdce2);
    box-shadow: 0 1px 3px rgba(0,0,0,0.35);
  }

  .inspiration { left: 47px; top: 283px; width: 381px; height: 271px; }
  .flag-tray {
    position: absolute; left: 33px; top: 54px; width: 312px; height: 194px;
    background: var(--tray);
    box-shadow: 0 3px 8px rgba(60,60,120,0.4);
  }
  .flag {
    position: absolute; width: 86px; height: 60px;
    border: 2px solid #ffffff;
    box-shadow: 0 2px 4px rgba(0,0,0,0.35);
    overflow: hidden;
  }
  .flag .band { flex: 1; }
  .flag.striped { display: flex; }
  .flag.horizontal { flex-direction: column; }
  .flag-caption { position: absolute; left: 9px; top: 80px; width: 86px; text-align: center; font-size: 13px; }

  .output {
    position: absolute; left: 459px; top: 94px; width: 313px; height: 460px;
    background: linear-gradient(180deg, var(--output-top), var(--output-bottom));
    opacity: 0.95;
  }
  .output-name {
    position: absolute; left: 0; right: 0; top: 170px; text-align: center;
    font-size: 58px; color: var(--ink-soft); letter-spacing: 1px;
  }

  .names {
    position: absolute; left: 815px; top: 88px; width: 319px; height: 467px;
    background: linear-gradient(180deg, rgba(220,200,235,0.85), rgba(190,205,240,0.75));
    border: 1px solid #ffffff;
    box-shadow: 0 2px 6px rgba(60,60,120,0.3);
  }
  .names-header {
    position: absolute; left: 12px; top: 11px; width: 296px; height: 39px;
    background: var(--panel);
    border-top: 1px solid #6f6fa8; border-bottom: 1px solid #6f6fa8;
    text-align: center; font-size: 20px; line-height: 37px;
  }
  .letter-bar {
    position: absolute; left: 12px; top: 52px; width: 296px; height: 20px;
    background: linear-gradient(180deg, #c8c8cc, #8f9096);
    font-size: 15px; line-height: 20px; padding-left: 6px;
  }
  .name-list { position: absolute; left: 12px; top: 50px; width: 280px; list-style: none; }
  .name-list li {
    height: 40.5px; border-bottom: 1px solid var(--rule);
    font-family: "Lato", "Helvetica", sans-serif; font-size: 16px; color: var(--ink);
    padding: 17px 0 0 10px; line-height: 20px;
  }
  .alpha-index {
    position: absolute; left: 290px; top: 56px; width: 16px; list-style: none; text-align: center;
    font-family: "Lato", "Helvetica", sans-serif; font-size: 9px; line-height: 12.9px; color: var(--index);
  }
  .favourites-bar {
    position: absolute; left: 4px; bottom: 4px; width: 309px; height: 41px;
    background: var(--panel-deep);
    text-align: center; font-size: 20px; line-height: 41px;
  }
  .favourites-bar svg { vertical-align: -3px; margin-left: 12px; }
</style>
</head>
<body>
  <svg class="backdrop" width="1200" height="585" viewBox="0 0 1200 585" aria-hidden="true">
    <polygon points="0,70 48,290 48,555 0,585" fill="#ffffff" opacity="0.12"/>
    <polygon points="1200,70 1140,290 1140,555 1200,585" fill="#ffffff" opacity="0.12"/>
  </svg>

  <section class="panel gender">
    <h2 class="panel-title">Select Gender</h2>
    <div class="gender-button boy"></div>
    <div class="gender-button girl"></div>
    <span class="gender-label boy">BOY</span>
    <span class="gender-label girl">GIRL</span>
  </section>

  <section class="panel speed">
    <span class="speed-label slower">SLOWER</span>
    <div class="speed-track"></div>
    <div class="speed-knob"></div>
    <span class="speed-label faster">FASTER</span>
  </section>

  <section class="panel inspiration">
    <h2 class="panel-title">Inspiration</h2>
    <div class="flag-tray">
      <div class="flag striped horizontal" style="left:9px;top:8px">
        <span class="band" style="background:#f4f4f6"></span>
        <span class="band" style="background:#2a48a8"></span>
        <span class="band" style="background:#c8262e"></span>
      </div>
      <div class="flag" style="left:112px;top:8px;background:linear-gradient(180deg,#c9343c 0 12%,#f1f1f3 12% 24%,#c9343c 24% 36%,#f1f1f3 36% 48%,#c9343c 48% 60%,#f1f1f3 60% 72%,#c9343c 72% 84%,#f1f1f3 84%)" role="img" aria-label="Flag of the United States"></div>
      <div class="flag" style="left:218px;top:8px;background:linear-gradient(135deg,#e0443c,#c0262c)" role="img" aria-label="Flag of China"></div>
      <span class="flag-caption">US NAMES</span>
      <div class="flag striped" style="left:9px;top:111px">
        <span class="band" style="background:#2f8a4e"></span>
        <span class="band" style="background:#f4f4f6"></span>
        <span class="band" style="background:#e88a34"></span>
      </div>
      <div class="flag striped" style="left:112px;top:111px">
        <span class="band" style="background:#2f8a4e"></span>
        <span class="band" style="background:#f4f4f6"></span>
        <span class="band" style="background:#c8343a"></span>
      </div>
      <div class="flag" style="left:218px;top:111px;background:linear-gradient(180deg,#ee9a44 0 33%,#f4f4f6 33% 66%,#2f8a4e 66%)" role="img" aria-label="Flag of India"></div>
    </div>
  </section>

  <main class="output">
    <p class="output-name">GIULIA</p>
  </main>

  <aside class="names">
    <h2 class="names-header">NAMES</h2>
    <ul class="name-list">
      <li>Ada</li>
      <li>Anastasia</li>
      <li>Anna</li>
      <li>Annamaria</li>
      <li>Adriana</li>
      <li>Amalia</li>
      <li>Almata</li>
      <li>Andromeda</li>
    </ul>
    <div class="letter-bar">A</div>
    <ol class="alpha-index">
      <li>A</li><li>B</li><li>C</li><li>D</li><li>E</li><li>F</li><li>G</li><li>H</li><li>I</li>
      <li>J</li><li>K</li><li>L</li><li>M</li><li>N</li><li>O</li><li>P</li><li>Q</li><li>R</li>
      <li>S</li><li>T</li><li>U</li><li>V</li><li>W</li><li>X</li><li>Y</li><li>Z</li><li>#</li>
    </ol>
    <div class="favourites-bar">FAVOURITES
      <svg width="14" height="18" viewBox="0 0 14 18" aria-hidden="true"><polygon points="1,1 13,9 1,17" fill="none" stroke="#ffffff" stroke-width="1.5"/></svg>
    </div>
  </aside>

  <svg class="backdrop" width="1200" height="585" viewBox="0 0 1200 585" aria-hidden="true" style="pointer-events:none">
    <line x1="101" y1="579" x2="1189" y2="13" stroke="#a8a8b4" stroke-width="1.2"/>
  </svg>
</body>
</html>
```